Quorzo Landing Page & Logo

We are building a landing page for a new blockchain-based project called Quorzo. The site should look modern and minimalistic with a very brief description of the upcoming project ("Unlock your Belmitra governance stack. Win weekly prizes and a quarterly jackpot!"), a viper logo (the animal - but can just be lettering) , and a button to subscribe for updates and early access.
Examples of similar pages:
https://pellow.finance/
https://www.trunemo.org/
https://merbisket.com/
https://k7.io/
https://www.drinnet.finance/
Target Market(s)
Crypto Users (Specifically Belmitra holders)
Coding
Coded - Design and coding required
Number of Pages Required
1 page
Look and feel
Each slider illustrates characteristics of the customer's brand and the style your logo design should communicate.

```html
<!DOCTYPE html>
<html lang="en">
<head>
<meta charset="utf-8">
<title>Quorzo</title>
<link href="https://fonts.googleapis.com/css2?family=Roboto:wght@400;500;700;900&family=Roboto+Slab:wght@400;700&display=swap" rel="stylesheet">
<style>
:root{
  --bg:#040a1c;
  --bg-header:#0a1022;
  --bg-band:#0a1226;
  --tile:#121a2e;
  --field:#1b2236;
  --green:#2ee87e;
  --white:#ffffff;
  --text:#e6e9f0;
  --rule:#1d2438;
}
*{margin:0;padding:0;box-sizing:border-box}
html,body{width:1200px;height:2235px;overflow:hidden;background:var(--bg);color:var(--white);font-family:'Roboto',sans-serif}
.page{position:relative;width:1200px;height:2235px;background:
  radial-gradient(ellipse 700px 420px at 1150px 250px,rgba(40,60,90,.25),transparent 70%),
  radial-gradient(ellipse 500px 400px at 80px 420px,rgba(40,60,90,.18),transparent 70%),
  var(--bg)}
.abs{position:absolute}
/* header */
.site-header{position:absolute;left:0;top:0;width:1200px;height:87px;border-bottom:1px solid var(--rule);background:rgba(10,16,34,.6)}
.brand{position:absolute;left:111px;top:14px;width:204px;text-align:center}
.brand-name{font-weight:900;font-size:36px;letter-spacing:1px;line-height:1;color:var(--white)}
.brand-tag{font-size:9px;margin-top:4px;color:var(--text);white-space:nowrap}
.main-nav{position:absolute;left:446px;top:35px;display:flex;gap:25px;font-size:14px;font-weight:500}
.main-nav a{color:var(--white);text-decoration:none;position:relative}
.main-nav a.active::after{content:"";position:absolute;left:0;right:0;top:47px;height:3px;background:var(--green)}
.socials{display:flex;gap:7px}
.socials span{width:36px;height:36px;border-radius:50%;background:var(--white)}
.socials span.first{background:var(--green)}
.header-socials{position:absolute;left:968px;top:26px}
/* hero */
.hero-title{left:111px;top:260px;font-family:'Roboto Slab',serif;font-weight:700;font-size:38px}
.hero-text{left:111px;top:327px;width:480px;font-size:19.5px;font-weight:500;line-height:31px}
.btn{display:inline-block;background:var(--green);color:#07101e;font-weight:700;text-align:center;border-radius:3px}
.hero-btn{left:111px;top:420px;width:146px;height:51px;line-height:51px;font-size:15px}
.hero-art{left:620px;top:178px;width:469px;height:382px;border-radius:40px;background:radial-gradient(ellipse at 50% 55%,#22b6d8 0%,#1a6fb0 35%,rgba(8,30,70,.4) 65%,transparent 75%)}
/* sections */
.section-title{left:0;width:1200px;text-align:center;font-family:'Roboto Slab',serif;font-size:36px}
.section-title.bold{font-weight:700}
.underline{height:2px;background:linear-gradient(90deg,transparent,var(--green) 15%,var(--green) 85%,transparent)}
.project-img{top:822px;width:476px;height:325px}
.img-city{left:111px;background:radial-gradient(ellipse at 50% 45%,#3b7fd6,#16378a 45%,#081838 85%)}
.img-servers{left:613px;background:linear-gradient(90deg,#0d3a5a 0%,#0c2238 35%,#1a2a40 60%,#6a4a3a 75%,#1b6070 100%)}
.project{top:1180px;width:476px;text-align:center}
.project h3{font-size:17.5px;font-weight:700;margin-bottom:12px}
.project p{font-size:14px;line-height:26px;color:var(--text);padding:0 28px}
.investor{top:1473px;width:179px;height:104px;background:var(--tile);display:flex;align-items:center;justify-content:center;font-weight:700;font-size:18px;color:var(--text);letter-spacing:1px}
.news-band{left:0;top:1640px;width:1200px;height:300px;background:radial-gradient(ellipse 650px 200px at 600px 150px,rgba(30,42,70,.55),transparent 75%)}
.subscribe-form{left:214px;top:1825px;width:771px;height:51px;background:var(--field);border-radius:4px}
.subscribe-form .field{position:absolute;left:16px;top:0;line-height:51px;font-size:16px;color:var(--text)}
.subscribe-form .btn{position:absolute;left:630px;top:4px;width:137px;height:43px;line-height:43px;border-radius:2px;font-size:15px}
/* footer */
.footer-brand{left:0;top:1980px;width:1200px;text-align:center}
.footer-brand .brand-name{font-size:52px}
.footer-brand .brand-tag{font-size:13px;margin-top:6px}
.footer-nav{left:0;width:1200px;text-align:center;font-size:17px;color:var(--white)}
.footer-nav span.sep{margin:0 20px}
.footer-nav.small{font-size:15.5px}
.footer-rule{left:111px;top:2171px;width:978px;height:1px;background:var(--rule)}
.copyright{left:0;top:2187px;width:1200px;text-align:center;font-size:13.5px}
.footer-socials{position:absolute;left:968px;top:2178px}
</style>
</head>
<body>
<div class="page">
  <header class="site-header">
    <div class="brand">
      <div class="brand-name">QUORZO</div>
      <div class="brand-tag">UNLOCK YOUR GOVERANCE BELMITRAs. WIN BIG.</div>
    </div>
    <nav class="main-nav">
      <a class="active">HOME</a><a>ABOUT</a><a>UPCOMING PROJECTS</a><a>INVESTORS</a><a>CONTACT</a>
    </nav>
    <div class="socials header-socials" aria-label="Social links"><span class="first"></span><span></span><span></span></div>
  </header>

  <h1 class="abs hero-title">WELCOME TO QUORZO</h1>
  <p class="abs hero-text">Lorem ipsum dolor sit amet, consectetur adipiscing elit, sed do eiusmod temporea.</p>
  <a class="abs btn hero-btn">GET STARTED</a>
  <div class="abs hero-art" role="img" aria-label="Isometric illustration of blockchain nodes and a coin vault"></div>

  <h2 class="abs section-title" style="top:712px">UPCOMING PROJECTS</h2>
  <div class="abs underline" style="left:507px;top:772px;width:186px"></div>
  <div class="abs project-img img-city" role="img" aria-label="Digital city of glowing data towers"></div>
  <div class="abs project-img img-servers" role="img" aria-label="Server racks with code overlay"></div>
  <div class="abs project" style="left:111px"><h3>SED UT PERSPICIATIS UNDE OMNIS</h3><p>Lorem ipsum dolor sit amet, consectetur adipiscing elit, sed do eiusmod tempor incididunt ut labore et dolore magna aliqua. Ut enim ad minim veniamea.</p></div>
  <div class="abs project" style="left:613px"><h3>SED UT PERSPICIATIS UNDE OMNIS</h3><p>Lorem ipsum dolor sit amet, consectetur adipiscing elit, sed do eiusmod tempor incididunt ut labore et dolore magna aliqua. Ut enim ad minim veniamea.</p></div>

  <h2 class="abs section-title bold" style="top:1370px">OUR INVESTORS</h2>
  <div class="abs underline" style="left:538px;top:1431px;width:126px"></div>
  <div class="abs investor" style="left:111px">TOVRELL</div>
  <div class="abs investor" style="left:311px">KESTIVA</div>
  <div class="abs investor" style="left:510px">MORVANE</div>
  <div class="abs investor" style="left:710px">PELQUIST</div>
  <div class="abs investor" style="left:910px">ZANDORO</div>

  <div class="abs news-band"></div>
  <h2 class="abs section-title bold" style="top:1724px;font-size:33px">SUBSCRIBE OUR NEWSLETTER</h2>
  <div class="abs underline" style="left:503px;top:1780px;width:195px"></div>
  <div class="abs subscribe-form">
    <span class="field">Email Address</span>
    <span class="btn">SUBSCRIBE</span>
  </div>

  <footer>
    <div class="abs footer-brand">
      <div class="brand-name">QUORZO</div>
      <div class="brand-tag">UNLOCK YOUR GOVERANCE BELMITRAs. WIN BIG.</div>
    </div>
    <div class="abs footer-nav" style="top:2085px">HOME<span class="sep">|</span>ABOUT<span class="sep">|</span>UPCOMING PROJECTS<span class="sep">|</span>INVESTORS<span class="sep">|</span>CONTACT</div>
    <div class="abs footer-nav small" style="top:2125px">PRIVACY POLICY<span class="sep">|</span>TERMS OF USE<span class="sep">|</span>LEGAL SUPPORT</div>
    <div class="abs footer-rule"></div>
    <div class="abs copyright">© 2022 <b>QUORZO</b> &nbsp;|&nbsp; All Rights Reserved</div>
    <div class="socials footer-socials" aria-label="Social links"><span class="first"></span><span></span><span></span></div>
  </footer>
</div>
</body>
</html>
```